QuadLantern--Help Us look fresh and new to companies, college students and college career centers!

We just designed a new logo and would like to freshen-up and make our business cards a bit more modern. Not crazy-modern like Picasso, but modern like metro-style and fresh like fruit. We use three logos with a combination of two colors each, and three colors total. We are looking for a single format to apply to three different cards/color schemes (green/blue to give out to companies, orange/green for students, and orange/blue for university career centers). Thanks everyone--looking forward to seeing your designs!!

Target Market(s)

Three styles: companies, college students/grads, college career centers

Industry/Entity Type

College

Contact Information for Business Card

Address: 1187 9th Avenue, Suite 614, Seattle, WA 98104. Need a spot for email address, web address (www.quadlantern-example.com), and phone numbers (main, direct, mobile). Don't open that website unless you want to lose your lunch--it is waaaay old and outdated. See this link instead, http://staging.brixelworks-example.com/QuadLantern/EmployerSolutions, for our new website design in progress.

Font styles to use
Sans Serif

Requirements
Must have
• Please use the logos supplied. Would like text to be grey but printable, like a "light" type style that is metro-type with sans-serif. NOT black text. Modern. For inspiration, here's a link to our work-in-progress website we are planning to launch soon: http://staging.brixelworks-example.com/QuadLantern/EmployerSolutions
Nice to have
• Would like to see something unique and different in a "metro" style. Clean and not cluttered.
Should not have
• No odd-sized cards

```html
<!DOCTYPE html>
<html lang="en">
<head>
<meta charset="utf-8">
<title>QuadLantern Business Cards</title>
<link href="https://fonts.googleapis.com/css2?family=Jost:ital,wght@0,300;0,400;0,600;1,500&display=swap" rel="stylesheet">
<style>
  :root {
    --backdrop: #e9e6e1;
    --card: #ffffff;
    --blue: #0a7cc4;
    --green: #7cc242;
    --grey: #6b6b6b;
    --pattern-blue: #e3eef8;
    --pattern-green: #eef5e6;
  }
  * { margin: 0; padding: 0; box-sizing: border-box; }
  html, body {
    width: 1200px; height: 900px; overflow: hidden;
    background: var(--backdrop);
    font-family: "Jost", "Helvetica Neue", Arial, sans-serif;
  }
  .canvas { position: relative; width: 1200px; height: 900px; }
  .card {
    position: absolute;
    width: 640px; height: 366px;
    background: var(--card);
    border-radius: 22px;
    overflow: hidden;
    box-shadow: 0 14px 30px rgba(0,0,0,0.18);
  }
  /* Back side */
  .card-back { left: 420px; top: 50px; }
  .back-pattern {
    position: absolute; inset: 0;
    background: linear-gradient(135deg, var(--pattern-blue) 0%, var(--pattern-green) 50%, var(--pattern-blue) 100%);
  }
  .back-brand {
    position: absolute; left: 0; right: 0; top: 150px;
    display: flex; justify-content: center; align-items: center; gap: 12px;
  }
  .brand-dot {
    width: 34px; height: 34px; border-radius: 50%;
    background: var(--green);
  }
  .back-brand .brand-name {
    font-size: 40px; font-weight: 600; color: var(--blue); letter-spacing: -0.5px;
  }
  /* Front side */
  .card-front { left: 140px; top: 470px; }
  .contact {
    position: absolute; right: 36px; top: 52px;
    text-align: right; color: var(--grey);
    font-weight: 300; font-size: 17px; line-height: 1.3;
  }
  .contact .person-name { color: var(--blue); font-weight: 400; font-size: 25px; line-height: 1.1; }
  .contact .person-role { color: var(--green); font-weight: 500; font-style: italic; font-size: 17px; margin-bottom: 12px; }
  .contact .line { display: flex; justify-content: flex-end; align-items: center; gap: 8px; }
  .contact .icon { width: 16px; height: 16px; flex: none; }
  .front-brand {
    position: absolute; left: 40px; bottom: 34px;
    display: flex; align-items: center; gap: 12px;
  }
  .front-brand .brand-dot { width: 40px; height: 40px; }
  .front-brand .brand-name {
    font-size: 54px; font-weight: 600; color: var(--blue); letter-spacing: -1px; line-height: 1;
  }
</style>
</head>
<body>
<div class="canvas">

  <section class="card card-back">
    <div class="back-pattern" role="img" aria-label="Faint repeating brand pattern in pale blue and pale green"></div>
    <div class="back-brand">
      <span class="brand-dot"></span>
      <span class="brand-name">QuadLantern</span>
    </div>
  </section>

  <section class="card card-front">
    <div class="contact">
      <div class="person-name">Dana Whitlow</div>
      <div class="person-role">Director</div>
      <div class="line">1187 9th Avenue</div>
      <div class="line">Suite 614</div>
      <div class="line">Seattle, WA 98104</div>
      <div class="line">206 555 0147
        <svg class="icon" viewBox="0 0 16 16"><path d="M3 5c0-2 10-2 10 0v1h-3V5H6v1H3z M4 8h8l1 5H3z" fill="var(--green)"/></svg>
      </div>
      <div class="line">206 555 0192
        <svg class="icon" viewBox="0 0 16 16"><rect x="4" y="1" width="8" height="14" rx="1.5" fill="none" stroke="var(--green)" stroke-width="1.8"/></svg>
      </div>
      <div class="line">info@quadlantern-example.com
        <svg class="icon" viewBox="0 0 16 16"><rect x="1" y="3" width="14" height="10" fill="var(--green)"/><path d="M1 3l7 6 7-6" fill="none" stroke="#fff" stroke-width="1.4"/></svg>
      </div>
      <div class="line">www.quadlantern-example.com
        <svg class="icon" viewBox="0 0 16 16"><circle cx="8" cy="8" r="6.5" fill="none" stroke="var(--green)" stroke-width="1.6"/><path d="M1.5 8h13M8 1.5c-3 3.5-3 9.5 0 13M8 1.5c3 3.5 3 9.5 0 13" fill="none" stroke="var(--green)" stroke-width="1.2"/></svg>
      </div>
    </div>
    <div class="front-brand">
      <span class="brand-dot"></span>
      <span class="brand-name">QuadLantern</span>
    </div>
  </section>

</div>
</body>
</html>
```